Modern brochure by Lawyers, for modern clients

It'sa "News" for their clients. Attached you can find the current News without design. It must be elegant but very attractive and modern. Their web site is http://www.montalbanyasociados.cl/ Their expertise is labor and employment practice area. It must be in editable format so that lawyers can write the news in a template with this corporate design.

Target Market(s)

Big Companies

Font styles to use
Sans Serif

Colors
0255a3
474747

Requirements
Nice to have
• Legal Pictures and only a little of yellow. One touch! It must be in editable format so that lawyers can write the news in a template with this corporate design.

```html
<!DOCTYPE html>
<html lang="es">
<head>
<meta charset="utf-8">
<title>Montalbán y Asociados — Noticias</title>
<link rel="stylesheet" href="https://fonts.googleapis.com/css2?family=EB+Garamond:wght@400;600;700&display=swap">
<style>
  :root {
    --stage: #6b6b6b;
    --paper: #ffffff;
    --brand-blue: #0b3f8e;
    --brand-blue-deep: #062c6b;
    --accent-yellow: #f3de1c;
    --ink: #474747;
    --ink-heading: #2d4a7a;
  }
  * { margin: 0; padding: 0; box-sizing: border-box; }
  html, body { width: 1200px; height: 1200px; overflow: hidden; }
  body {
    background: var(--stage);
    font-family: "EB Garamond", Georgia, serif;
    color: var(--ink);
    position: relative;
  }
  .newsletter {
    position: absolute;
    left: 175px; top: 50px;
    width: 850px; height: 1100px;
    background: var(--paper);
    overflow: hidden;
  }
  .newsletter__backdrop { position: absolute; inset: 0; }
  .newsletter__photo { position: absolute; left: 500px; top: 720px; }
  .date-line {
    position: absolute; right: 50px; top: 40px;
    color: #fff; font-weight: 600; font-size: 19px;
    text-align: right; line-height: 1.25;
  }
  .brand {
    position: absolute; left: 70px; top: 118px;
    display: flex; align-items: center; gap: 18px;
  }
  .brand__dot {
    width: 52px; height: 52px; border-radius: 50%;
    background: var(--ink-heading);
  }
  .brand__name {
    font-size: 34px; font-weight: 400; letter-spacing: 2px;
    color: var(--ink-heading); text-transform: uppercase;
  }
  .letter {
    position: absolute; left: 88px; top: 222px; width: 690px;
    font-size: 16.5px; line-height: 1.3;
  }
  .letter__greeting {
    font-size: 30px; color: var(--ink-heading); font-weight: 400;
    margin: 0 0 12px -10px;
  }
  .letter p { margin-bottom: 18px; }
  .letter__link {
    color: var(--brand-blue); font-weight: 700;
    text-decoration: underline; text-decoration-thickness: 2px;
  }
  .letter__closing { padding-left: 14px; }
  .signature { margin: -4px 0 0 30px; }
  .signature__firm {
    font-size: 25px; font-weight: 700; color: var(--brand-blue); line-height: 1.2;
  }
  .signature__mail {
    display: flex; align-items: center; gap: 8px;
    font-size: 16px; font-weight: 700; color: var(--brand-blue);
  }
  .contact-band {
    position: absolute; left: 60px; bottom: 60px; color: #fff;
  }
  .contact-band__phone { font-size: 32px; font-weight: 700; }
  .contact-band__web { font-size: 20px; font-weight: 700; }
</style>
</head>
<body>
<article class="newsletter">
  <svg class="newsletter__backdrop" width="850" height="1100" viewBox="0 0 850 1100" aria-hidden="true">
    <defs>
      <linearGradient id="bandBlue" x1="0" y1="0" x2="1" y2="1">
        <stop offset="0" stop-color="#1b57ad"/>
        <stop offset="1" stop-color="#062c6b"/>
      </linearGradient>
      <linearGradient id="mistFade" x1="0" y1="0" x2="0" y2="1">
        <stop offset="0" stop-color="#dfe4ea"/>
        <stop offset="1" stop-color="#ffffff"/>
      </linearGradient>
      <radialGradient id="gavelTone" cx="0.5" cy="0.55" r="0.6">
        <stop offset="0" stop-color="#b48a4e"/>
        <stop offset="0.55" stop-color="#e8d9a8"/>
        <stop offset="1" stop-color="#ffffff"/>
      </radialGradient>
    </defs>
    <rect x="0" y="0" width="850" height="330" fill="url(#mistFade)"/>
    <path d="M520 0 H850 V430 C800 250 690 80 520 0 Z" fill="url(#bandBlue)"/>
    <path d="M430 0 C640 60 790 200 850 430 V470 C770 240 620 80 400 0 Z" fill="#fff"/>
    <path d="M470 0 C680 70 810 230 850 430 C780 210 660 70 520 0 Z" fill="var(--accent-yellow)"/>
    <path d="M0 600 C90 900 300 1000 560 1100 H0 Z" fill="url(#bandBlue)"/>
    <path d="M0 560 C60 860 300 990 620 1100 H560 C300 1000 90 900 0 600 Z" fill="#fff"/>
    <path d="M0 575 C70 870 300 995 600 1100 H560 C300 1000 90 900 0 600 Z" fill="var(--accent-yellow)"/>
  </svg>
  <svg class="newsletter__photo" width="350" height="330" viewBox="0 0 350 330" role="img" aria-label="Fotografía de un mazo de juez de madera sobre un libro abierto">
    <rect width="350" height="330" fill="url(#gavelTone)"/>
  </svg>

  <div class="date-line">Santiago, 25 de julio<br>de 2018</div>

  <header class="brand">
    <span class="brand__dot"></span>
    <span class="brand__name">Montalbán y Asociados</span>
  </header>

  <section class="letter">
    <h1 class="letter__greeting">Estimados,</h1>
    <p>Por medio del presente, les damos a conocer el Dictamen Ordinario N° 3826-031, emitido por la Dirección del Trabajo el pasado 20 de julio, relativo a los “beneficios históricos”.</p>
    <p>Estos fueron definidos en su oportunidad por este organismo como “…aquellos beneficios que se han otorgado desde siempre…” por parte del empleador.</p>
    <p>A partir de este Dictamen, el cual reconsidera el criterio del anterior Director del Trabajo, los beneficios históricos vuelven a ser patrimonio de la empresa y de los trabajadores que los han recibido, dejando de serlo de la organización sindical y de sus socios beneficiados por el solo hecho de haberse “replicado” en un instrumento colectivo durante una negociación.</p>
    <p>Por último, el Dictamen en comento aclara que si un “beneficio histórico” se incrementa de manera real y efectiva producto de una negociación colectiva, únicamente dicho incremento se entenderá originado en el respectivo instrumento colectivo, y en consecuencia, objeto de una posible extensión en el evento de que ésta se haya acordado durante la negociación.</p>
    <p>Para mayor análisis de lo resuelto por la Dirección del Trabajo, se puede revisar el Dictamen en comento <a class="letter__link" href="http://www.montalbanyasociados.cl/">haciendo click aquí</a></p>
    <p class="letter__closing">Sin otro particular, saluda atentamente a ustedes,</p>
    <footer class="signature">
      <div class="signature__firm">Montalbán y Asociados</div>
      <div class="signature__mail">
        <svg width="16" height="12" viewBox="0 0 16 12" aria-hidden="true"><rect width="16" height="12" rx="1" fill="var(--brand-blue)"/><path d="M1 1 L8 7 L15 1" stroke="#fff" stroke-width="1.5" fill="none"/></svg>
        oficina@montalbanyasociados.cl
      </div>
    </footer>
  </section>

  <div class="contact-band">
    <div class="contact-band__phone">+562 2987 4410</div>
    <div class="contact-band__web">www.montalbanyasociados.cl</div>
  </div>
</article>
</body>
</html>
```